Medical device box for kits used for self testing purposes. Attractive simplistic design

Looking for a design that will go on a box that offer multiple range of medical testing ranging from hormones panel to diabetes and thyroid hormones. looking for something attractive and simple to go on a box 6 x 4.5 x 1 inches. attached are some examples from competitors. and our logo that be incorporated with the design.
Picture of the boxes have been attached, pick the color you think goes best with your design.

Target Market(s)

Patients and regular consumers

Industry/Entity Type

Medical

Requirements
Nice to have
• Simple design that is eye catching

```html
<!DOCTYPE html>
<html lang="en">
<head>
<meta charset="utf-8">
<title>Veridan – Food Sensitivity Comprehensive Test</title>
<link rel="stylesheet" href="https://fonts.googleapis.com/css2?family=Figtree:wght@400;500;700;800&display=swap">
<style>
  :root {
    --navy: #1c2141;
    --white: #ffffff;
    --sun: #fcc72c;
    --lemon: #f7e51b;
    --pale-sun: #fde9a6;
  }
  * { margin: 0; padding: 0; box-sizing: border-box; }
  html, body {
    width: 1200px;
    height: 960px;
    overflow: hidden;
    background: var(--white);
  }
  .box-face {
    position: relative;
    width: 1200px;
    height: 960px;
    background: var(--white);
    color: var(--navy);
    font-family: "Figtree", sans-serif;
  }
  .brand {
    position: absolute;
    left: 97px;
    top: 145px;
    height: 100px;
    display: flex;
    align-items: center;
    gap: 18px;
  }
  .brand-dot {
    width: 64px;
    height: 64px;
    border-radius: 50%;
    background: var(--sun);
  }
  .brand-name {
    font-size: 86px;
    font-weight: 800;
    line-height: 1;
    letter-spacing: -1px;
    color: var(--navy);
  }
  .product-title {
    position: absolute;
    left: 97px;
    top: 384px;
    font-size: 62px;
    font-weight: 700;
    line-height: 84px;
    letter-spacing: 0.3px;
  }
  .title-rule {
    position: absolute;
    left: 99px;
    top: 597px;
    width: 150px;
    height: 5px;
    border-radius: 3px;
    background: var(--lemon);
  }
  .product-summary {
    position: absolute;
    left: 97px;
    top: 630px;
    font-size: 34px;
    font-weight: 400;
    line-height: 46px;
  }
  .feature-list {
    position: absolute;
    left: 97px;
    top: 816px;
    display: flex;
    gap: 62px;
    list-style: none;
  }
  .feature {
    display: flex;
    align-items: center;
    gap: 14px;
    font-size: 23.5px;
    font-weight: 500;
  }
  .feature-icon { width: 64px; height: 70px; }
  .art-placeholder {
    position: absolute;
    left: 723px;
    top: 0;
    width: 395px;
    height: 960px;
    background: linear-gradient(180deg, var(--pale-sun) 0%, var(--sun) 55%, var(--pale-sun) 100%);
  }
</style>
</head>
<body>
<main class="box-face">
  <div class="brand">
    <span class="brand-dot"></span>
    <span class="brand-name">Veridan</span>
  </div>

  <h1 class="product-title">Food Sensitivity<br>Comprehensive Test</h1>
  <div class="title-rule"></div>

  <p class="product-summary">Lorem ipsum dolor sit amet,<br>consectetur adipiscing elit, sed do</p>

  <ul class="feature-list">
    <li class="feature">
      <svg class="feature-icon" viewBox="0 0 64 70" aria-hidden="true">
        <polygon points="32,3 60,19 60,51 32,67 4,51 4,19" fill="none" stroke="var(--navy)" stroke-width="1.5"/>
        <polygon points="32,8 55,21.5 55,48.5 32,62 9,48.5 9,21.5" fill="none" stroke="var(--navy)" stroke-width="1"/>
        <path d="M32 44 c-8 -5 -12 -9 -12 -14 a6 6 0 0 1 12 -2 a6 6 0 0 1 12 2 c0 5 -4 9 -12 14 z" fill="none" stroke="var(--navy)" stroke-width="1.6"/>
        <path d="M41 21 h6 M44 18 v6" stroke="var(--navy)" stroke-width="1.6"/>
      </svg>
      <span>Lorem ipsum dolor</span>
    </li>
    <li class="feature">
      <svg class="feature-icon" viewBox="0 0 64 70" aria-hidden="true">
        <polygon points="32,3 60,19 60,51 32,67 4,51 4,19" fill="none" stroke="var(--navy)" stroke-width="1.5"/>
        <polygon points="32,8 55,21.5 55,48.5 32,62 9,48.5 9,21.5" fill="none" stroke="var(--navy)" stroke-width="1"/>
        <path d="M32 22 l11 4 v8 c0 7 -5 11 -11 13 c-6 -2 -11 -6 -11 -13 v-8 z" fill="none" stroke="var(--navy)" stroke-width="1.6"/>
        <path d="M29 30 h6 v4 h4 v5 h-4 v4 h-6 v-4 h-4 v-5 h4 z" fill="none" stroke="var(--navy)" stroke-width="1.3"/>
      </svg>
      <span>Lorem ipsum dolor</span>
    </li>
  </ul>

  <div class="art-placeholder" role="img" aria-label="Decorative artwork area: flowing helix of yellow dots with intertwined coloured ribbons"></div>
</main>
</body>
</html>
```